Interactive Children's Media Book Company Website Design

We need a website DESIGN (no coding required) for a new interactive children's media book company called Tovira Studios.

We develop high-quality interactive children's books for the iPad/iPhone that seeks to delight and inspire young and old alike. Our stories are filled with heart and spirit, and we seek to breathe magic back into books so that people fall back in love with reading.

Tovira means "butterfly" in Korean. It plays on the idea that a caterpillar metamorphoses into a butterfly - and in the same way, our readers are transformed through the journey of experiencing our interactive books.

We're looking for something based on the ATTACHED LOGO DESIGN for our company. A website that's professional, modern, fun and inviting; easy to read and not-cluttered, but still portraying the feeling of innocence and childhood.

We're looking for something that resonates the magical experience we want to create for our readers. Specific requirements on pages, tabs, content, etc are below.

Industry/Entity Type

It Company

Requirements
Nice to have
• There are 7 tabs on the Homepage of the website: HOME, GRANDPA, ABOUT US, CAREERS, NEWS, CONTACT US, SHOP. (But there is an extra page called THEIR GARDEN, which will be a sub-page under Grandpa).

HOME
• Would be great to have some key images of our book (3-4 screen shots) as the key focus of the homepage that automatically scroll through every few seconds. (Placeholder image attached). The images would link to the “Grandpa” page.
• Company logo (attached to brief) and slogan: “A new era of children’s media” quite prominent on page.
• Key text content to be on page: “Tovira means “butterfly” in Korean. Just as a caterpillar transforms into a butterfly, Tovira Studios takes the reader on an unforgettable journey of metamorphosis through our stories. We turn children’s books into a high-quality interactive experience on mobile platforms - breathing magic back into books, and inspiring people to fall back in love with reading. Through our unique characters full of heart and spirit, our stories delight and inspire young and old alike.”
• Twitter & Facebook Like & Facebook page link icons.
• Section on Latest News with a few of the latest entries.
• Section on latest sister images & comments that visitors have posted, which takes you to the “Their Garden” page.

GRANDPA
• The title for this page is “Grandpa Keeps a Secret Garden”
• There will be a little iPad/iPhone icon (placeholder attached) for this book.
• There will be a link to the App Store to buy the app book.
• Key text content on this page: “Our debut interactive media book is coming soon on the iPad and iPhone! “Grandpa Keeps a Secret Garden” touches on the beautiful and inextricable (albeit sometimes frustrating!) bond between sisters.”
• There will be a section on “Features” which lists all the various special features the app book includes.
• There will be a YouTube clip embedded into the page, which shows how the app book works.
• A section that says: “Do you have a sister who’s not like other sisters? Share a photo and tell us about her!” which links to the sub-page “Their Garden”.
• Under this, there may be the most recent few images submitted by the public, which when clicked on, would also link to the sub-page “Their Garden”.

THEIR GARDEN
• The main text on the page: “Do you have a sister who’s not like other sisters? Share a photo and tell us about her!”
• Main body of the page is a gallery of all the photos that have been submitted. If you click on each of the images, you get the comments that people have submitted with the photos.
• The page would also have a Submit Comments Form, where people can upload a picture of their sister(s) and write a comment to accompany the image.

ABOUT US
• Introductory text on page: “It was a chance conversation at Harbourview Terminal, where two friends discovered they shared a dream to create quality children's media. Both of them were excited by the possibilities of using new digital platforms to inspire and educate a younger generation. From that idea Tovira Studios was born. We seek to be the chrysalis of story telling - to inspire the hearts and minds of our generation, and generations to come.”
• Section to “Join the Mailing List” where they can put their email address in and submit.
• Bios of 2x people with photos (bios in word doc attached) (do not have photos yet).

CAREERS
• The main text on the page: “We are always on the lookout for talented people to join our team. If you are a writer, illustrator, animator, iOS/android developer, musician, creative-writing translator - or have something special to offer Tovira Studios - we are keen to hear from you. Send us a message through the Contact Us tab above.”

NEWS
• Regular News page, with blog-type entries.

CONTACT US
• Online submit Contact Us form
• The main text on page: “Our studio is based in the Marram Arts Hub, 14 Pellham Street, Ardlow, Wellington. Marram is a professional, creative collective - with four separate studios, gallery, and retail store. For more information on Marram, visit: http://www.marramhub.example.nz”
• “We would love to hear from you! Whether you have questions, ideas, comments, or just want to say hullo - please leave us a message and we will get back to you soon.”
• Including image of the premises (Marram image attached to brief).

SHOP
• Where visitors can purchase merchandise (t-shirts, mugs, etc) of the book/company.

```html
<!DOCTYPE html>
<html lang="en">
<head>
<meta charset="utf-8">
<title>Tovira Studios – Their Garden</title>
<link rel="stylesheet" href="https://fonts.googleapis.com/css2?family=Arimo:wght@400;700&family=Comfortaa:wght@400;700&display=swap">
<style>
  :root {
    --page-bg-top: #d9d6dd;
    --page-bg-bottom: #c9c2d4;
    --panel-bg: #f4f2f6;
    --panel-border: #cfcad6;
    --ink: #4a4a4a;
    --ink-soft: #8a8a8a;
    --purple: #7d4fc0;
    --purple-light: #a98ad8;
    --nav-a: #8ec5de;
    --nav-b: #b7a4dc;
    --nav-c: #c6a2e6;
    --modal-bg: #ffffff;
    --modal-shadow: rgba(0,0,0,.35);
    --scene-sky: #8fcdea;
    --scene-grass: #7fb548;
    --scene-tree: #6b4a2a;
    --box-bg: #f0eff1;
    --dim: rgba(70,66,78,.48);
  }
  * { box-sizing: border-box; margin: 0; padding: 0; }
  html, body { width: 1200px; height: 777px; overflow: hidden; }
  body {
    position: relative;
    font-family: "Arimo", Arial, sans-serif;
    color: var(--ink);
    background: linear-gradient(180deg, var(--page-bg-top), var(--page-bg-bottom));
  }
  .abs { position: absolute; }

  /* header */
  .brand { left: 120px; top: 9px; width: 308px; height: 103px; display: flex; align-items: center; gap: 14px; }
  .brand-mark { width: 62px; height: 62px; border-radius: 50%; background: #b9a6dc; }
  .brand-name { font-family: "Comfortaa", sans-serif; font-size: 62px; font-weight: 400; color: #8c8c8c; letter-spacing: -1px; }
  .slogan { left: 457px; top: 31px; font-family: "Comfortaa", sans-serif; font-size: 22px; color: #8a8a8a; letter-spacing: .5px; }
  .social { top: 30px; width: 24px; height: 24px; border-radius: 3px; }
  .social-a { left: 1023px; background: #5a74a8; }
  .social-b { left: 1054px; background: #59b7e3; }
  .nav { left: 454px; top: 62px; width: 624px; height: 49px; border-radius: 8px;
    background: linear-gradient(90deg, var(--nav-a), var(--nav-b) 60%, var(--nav-c)); }
  .nav-item { position: absolute; top: 17px; font-size: 13px; font-weight: 700; color: #fff; letter-spacing: .3px; }
  .nav-item.current { top: 12px; padding: 5px 8px; border-radius: 12px; background: #e6e3e8; color: #555; }

  /* content */
  .panel { left: 120px; top: 133px; width: 960px; height: 598px; border: 2px solid var(--panel-border); border-radius: 12px; background: var(--panel-bg); }
  .page-title { left: 142px; top: 156px; font-size: 22px; color: var(--purple-light); }
  .lead { left: 142px; top: 196px; font-size: 12px; font-weight: 700; color: #555; }
  .section-title { left: 142px; font-size: 19px; color: #666; }
  .gallery { left: 142px; top: 263px; width: 915px; height: 174px; border: 1px solid #dcd8df; border-radius: 4px; background: #fff; }
  .form-box { left: 142px; top: 494px; width: 915px; height: 174px; border: 1px solid #dcd8df; border-radius: 4px; background: #fff; }
  .placeholder { left: 154px; top: 509px; font-size: 11px; color: #aaa; }
  .post-btn { left: 970px; top: 637px; width: 77px; height: 26px; border-radius: 8px; background: var(--purple-light); color: #fff; font-size: 12px; display: flex; align-items: center; justify-content: center; }
  .footer-rule { left: 124px; top: 747px; width: 952px; height: 1px; background: #999; }
  .copyright { left: 0; width: 1200px; top: 754px; text-align: center; font-size: 10px; color: #555; }

  .dim { inset: 0; background: var(--dim); }

  /* lightbox */
  .lightbox { left: 189px; top: 89px; width: 788px; height: 586px; background: var(--modal-bg); border-radius: 12px; box-shadow: 0 0 10px var(--modal-shadow); }
  .stage { left: 200px; top: 100px; width: 767px; height: 408px; background: #f8f6f6; }
  .artwork { left: 243px; top: 100px; width: 684px; height: 408px;
    background: linear-gradient(180deg, var(--scene-sky) 0%, #b9dcea 38%, #d5a866 52%, var(--scene-grass) 70%, #6da63e 100%); }
  .nav-arrow { top: 372px; width: 46px; height: 46px; }
  .meta { font-size: 11px; color: #333; }
  .link { font-size: 11px; color: var(--purple); }
  .like-box { left: 243px; top: 534px; width: 315px; height: 30px; background: var(--box-bg); display: flex; align-items: center; gap: 6px; padding-left: 10px; font-size: 11px; }
  .comment-box { left: 243px; top: 566px; width: 315px; height: 43px; background: var(--box-bg); padding: 5px 9px; font-size: 11px; line-height: 19px; }
  .comment-author { font-weight: 700; color: var(--purple); }
  .comment-time { color: #999; }
  .meta-rule { left: 715px; top: 567px; width: 252px; height: 1px; background: #e2e2e2; }
</style>
</head>
<body>
  <!-- background page -->
  <div class="abs brand"><span class="brand-mark"></span><span class="brand-name">Tovira</span></div>
  <div class="abs slogan">A new era of children’s media...</div>
  <span class="abs social social-a" aria-label="Social page link"></span>
  <span class="abs social social-b" aria-label="Social feed link"></span>

  <nav class="abs nav">
    <span class="nav-item" style="left:26px">HOME</span>
    <span class="nav-item current" style="left:87px">GRANDPA</span>
    <span class="nav-item" style="left:198px">ABOUT US</span>
    <span class="nav-item" style="left:296px">CAREERS</span>
    <span class="nav-item" style="left:388px">NEWS</span>
    <span class="nav-item" style="left:457px">CONTACT US</span>
    <span class="nav-item" style="left:572px">SHOP</span>
  </nav>

  <div class="abs panel"></div>
  <h1 class="abs page-title">Their Garden</h1>
  <p class="abs lead">Do you have a sister who’s not like other sisters? Share a photo and tell us about her!</p>
  <h2 class="abs section-title" style="top:232px">Photos</h2>
  <div class="abs gallery"></div>
  <h2 class="abs section-title" style="top:463px">Submit a Comment</h2>
  <div class="abs form-box"></div>
  <span class="abs placeholder">Say something</span>
  <span class="abs post-btn">Post</span>
  <div class="abs footer-rule"></div>
  <p class="abs copyright">Copyright © 2011 Tovira. All Rights Reserved</p>

  <div class="abs dim"></div>

  <!-- photo lightbox -->
  <div class="abs lightbox"></div>
  <div class="abs stage"></div>
  <div class="abs artwork" role="img" aria-label="Illustration of a girl on a trampoline in a sunny backyard with a tree, tyre swing and kennel"></div>

  <svg class="abs nav-arrow" style="left:131px" viewBox="0 0 46 46" aria-label="Previous photo">
    <circle cx="23" cy="23" r="21" fill="#fff" stroke="#666" stroke-width="2"/>
    <path d="M26 16 L18 23 L26 30 Z" fill="#333"/>
  </svg>
  <svg class="abs nav-arrow" style="left:989px" viewBox="0 0 46 46" aria-label="Next photo">
    <circle cx="23" cy="23" r="21" fill="#fff" stroke="#666" stroke-width="2"/>
    <path d="M20 16 L28 23 L20 30 Z" fill="#333"/>
  </svg>

  <a class="abs link" style="left:243px;top:517px">Share</a>
  <div class="abs like-box">
    <svg width="13" height="12" viewBox="0 0 13 12" aria-hidden="true">
      <rect x="0.5" y="5" width="3" height="6.5" fill="none" stroke="#4a63a0"/>
      <path d="M4 5.5 L7 1 Q8.5 1 8.2 3 L7.8 4.5 H11.5 Q12.5 5 12 6 L10.8 11 H4 Z" fill="none" stroke="#4a63a0"/>
    </svg>
    <span><span class="link">2 people</span> like this.</span>
  </div>
  <div class="abs comment-box">
    <div><span class="comment-author">User 1</span> nice Pic</div>
    <div class="comment-time">2 hours ago</div>
  </div>

  <p class="abs meta" style="left:715px;top:525px">Album:Profile Pictures · 1 of 2s</p>
  <p class="abs meta" style="left:715px;top:543px">Posted:14 hours ago</p>
  <div class="abs meta-rule"></div>
  <a class="abs link" style="left:715px;top:581px">Done Tagging</a>
  <a class="abs link" style="left:715px;top:600px">Download</a>
  <a class="abs link" style="left:715px;top:618px">Report This Photo</a>
</body>
</html>
```